GUARANTEED 4 sample word cards for inclusive primary education (the swan, the icebear, the cat, sad)

in short: it's about drawing a swan, at icebear, a cat, a sad person (male / female) and arranging them on word cards with some additional information As there which only one design submitted, Which was missing the point I Decided to translate everything myself and upload it again. Requirements Within an open educational ressources (OER) project, materials for the interest-based spelling workout are to be created. In the preparation of this project four example sample word cards are to be developed. Later They Should be compiled dynamically from a database. Since the needs of the teachers are very different, it would be advantageous to integrate the different design elements as layers in Photoshop so did one can show how diverse the cards can look later by hiding / showing the layers. The materials shoulderstand be distributed under cc-0 license. It is about 4 sample cards (the swan, the icebear, the cat, sad), Which shoulderstand demonstrate how search cards can look. German: As part of an OER project are materials to interest-based spelling learning occur. In the preparation of the project (to be created also a permanent position for a / n Designer / -in under which) are four examplarische Sample word cards are developed. Later this should be assembled dynamically from a database. Since the needs of teachers / -Innen are very different, it would be desirable to integrate the various design elements as layers in Photoshop, so you can show how diverse can look the cards later. The materials are to be distributed under cc-0 license. It is about 4 example cards that demonstrate how can such cards look. The most expensive part is undoubtedly the drawings (polar bear, swan, cat and sad child / sad person). Common elements - speech symbol Veldarini (see http: //media.lirobeck-press. example / media / catalog / product / cache / 4 / image / 3ab51cde90417f62c8e0a4d19253b78a / 0/7 / 04189_1.jpg) - underline articles colored or colored or point mark (male - red, male - blue, neuter - green) - writing of definition and article (once https://glyphshelf.example/en/font/grundschrift and once a school Ausgangsschrift eg https://www.tomvaro.example/hub/Lumen/de_DE.CMS.displayCMS.318406./die-schulausgangsschrift -sas-free-download-tomvaro) - Ruling based on http://www.b-straleck.example/wp-content/uploads/2010/01/Heft-006-innen.png (and even without house) - picture on the right side - pictures with people, each as a girl / boy, different skin colors (or all as layers in Photoshop, where I can hide it myself) - syllable sheets (instead of the | http://trymindquill.example/wp- content / uploads / 2015_2_Silbenboegen_Kombo.png) - colored syllables (blue and red) - stem color (red), ending black - cases if necessary on the back of the card - Format Din A7, rounded corners images should as svg / or levels exist (different skin color / hair color / gender) drawings should stylized and not be too childish and love of detail, so that they are attractive to adults (and as can be used in work with fugitives). You should also black / white and be usable with red / green blindness. The exact requirements are in the description file. For any questions please contact via the platform or haraldp.ostwig@hs-varnholt.example Ps: If a logo for (spelling) learning, including drops, it is also nich bad;) If you interested in a long-term employment in a project have the university, we appreciate if you mention this.
pupils in primary school, so but older students and adults (for example refugees who started to learn the language) students / -Innen primary school (until fourth grade) as well as older adolescents / adults, therefore, not to child pictures
Education
- see additional file

- psd files with levels, to show and hide different elements self drawn images, Which Could be released under a CC-0 license. see additional file for more info and sample German: .psd files with labeled layers, in which the individual elements can be hidden. Self-drawn graphics which can then be released under cc-0 Stock

```html
<!DOCTYPE html>
<html lang="de">
<head>
<meta charset="utf-8">
<title>Wortkarte – traurig</title>
<link rel="stylesheet" href="https://fonts.googleapis.com/css2?family=Andika&family=Fira+Sans:wght@400;500&family=Dancing+Script&display=swap">
<style>
  :root {
    --lime: #b2d334;
    --lime-pale: #e3efc6;
    --teal: #00a99d;
    --sage: #b8c692;
    --sage-text: #aebd84;
    --ink: #646464;
    --white: #ffffff;
    --backdrop: #ecebe8;
  }
  html, body {
    margin: 0;
    width: 931px;
    height: 1200px;
    overflow: hidden;
    background: var(--backdrop);
  }
  .word-card {
    position: absolute;
    left: 115px;
    width: 676px;
    height: 476px;
    background: var(--white);
    overflow: hidden;
    box-shadow: 0 3px 8px rgba(0,0,0,0.25);
  }
  .word-card--front { top: 111px; }
  .word-card--back { top: 631px; }
  .card-bands {
    position: absolute;
    inset: 0;
    width: 676px;
    height: 476px;
  }
  .speech-symbol {
    position: absolute;
    left: 29px;
    top: 38px;
    width: 73px;
    height: 120px;
    background: var(--sage);
    opacity: 0.55;
  }
  .headword {
    position: absolute;
    left: 122px;
    top: 98px;
    margin: 0;
    font-family: "Andika", sans-serif;
    font-weight: 400;
    font-size: 52px;
    line-height: 1;
    color: var(--ink);
  }
  .headword .article { color: var(--teal); }
  .meaning-list {
    position: absolute;
    left: 122px;
    top: 160px;
    margin: 0;
    padding: 0;
    list-style: none;
    font-family: "Andika", sans-serif;
    font-size: 38px;
    line-height: 46px;
    color: var(--ink);
  }
  .example-sentence {
    position: absolute;
    left: 112px;
    top: 308px;
    margin: 0;
    font-family: "Dancing Script", cursive;
    font-size: 26px;
    color: var(--teal);
  }
  .figure-sad {
    position: absolute;
    left: 383px;
    top: 115px;
    width: 252px;
    height: 228px;
    border-radius: 46% 40% 20% 50%;
    background: radial-gradient(ellipse at 60% 45%, var(--sage) 55%, rgba(184,198,146,0) 72%);
  }
  .comparison {
    position: absolute;
    left: 0;
    width: 560px;
    top: 424px;
    margin: 0;
    text-align: center;
    font-family: "Fira Sans", sans-serif;
    font-size: 24px;
    color: var(--white);
  }
  .word-type-mark {
    position: absolute;
    left: 565px;
    top: 409px;
    width: 37px;
    height: 33px;
  }
  .figure-sad--small {
    left: 37px;
    top: 22px;
    width: 100px;
    height: 95px;
  }
  .case-table {
    position: absolute;
    left: 34px;
    top: 103px;
    border-collapse: collapse;
  }
  .case-table th, .case-table td { padding: 0; height: 47px; vertical-align: middle; text-align: left; }
  .case-table thead th {
    height: 28px;
    font-family: "Fira Sans", sans-serif;
    font-weight: 500;
    font-size: 15px;
    letter-spacing: 0.5px;
    color: var(--sage-text);
  }
  .case-table .case-name {
    width: 297px;
    font-family: "Andika", sans-serif;
    font-weight: 400;
    font-size: 22px;
    color: var(--sage-text);
  }
  .case-table .singular { width: 182px; }
  .case-table td {
    font-family: "Fira Sans", sans-serif;
    font-size: 17px;
    color: var(--ink);
  }
</style>
</head>
<body>

<section class="word-card word-card--front">
  <svg class="card-bands" viewBox="0 0 676 476" aria-hidden="true">
    <path d="M88 0 H676 V86 C520 78 300 46 88 0 Z" fill="var(--lime-pale)"/>
    <path d="M88 0 H676 V74 C520 68 300 38 88 0 Z" fill="var(--lime)"/>
    <path d="M0 396 C220 360 460 362 676 392 V476 H0 Z" fill="var(--lime-pale)"/>
    <path d="M0 408 C220 376 460 378 676 406 V476 H0 Z" fill="var(--teal)"/>
  </svg>
  <div class="speech-symbol" role="img" aria-label="Sprechsymbol: Haus mit Treppe"></div>
  <h1 class="headword"><span class="article">die</span> trau|rig</h1>
  <ul class="meaning-list">
    <li>Stimmung</li>
    <li>Mensch</li>
    <li>Gefühl</li>
  </ul>
  <p class="example-sentence">Das Kind ist traurig.</p>
  <div class="figure-sad" role="img" aria-label="Silhouette einer traurig sitzenden Frau"></div>
  <p class="comparison">traurig, trauriger, am traurigsten</p>
  <svg class="word-type-mark" viewBox="0 0 37 33" aria-hidden="true">
    <polygon points="18.5,0 37,33 0,33" fill="var(--white)"/>
  </svg>
</section>

<section class="word-card word-card--back">
  <svg class="card-bands" viewBox="0 0 676 476" aria-hidden="true">
    <path d="M88 0 H676 V86 C520 78 300 46 88 0 Z" fill="var(--lime-pale)"/>
    <path d="M88 0 H676 V74 C520 68 300 38 88 0 Z" fill="var(--lime)"/>
    <path d="M0 392 C220 356 460 358 676 388 V476 H0 Z" fill="var(--lime-pale)"/>
    <path d="M0 404 C220 372 460 374 676 402 V476 H0 Z" fill="var(--teal)"/>
  </svg>
  <div class="figure-sad figure-sad--small" role="img" aria-label="Kleine Silhouette einer traurig sitzenden Frau"></div>
  <table class="case-table">
    <thead>
      <tr><th></th><th class="singular">SINGULAR</th><th>PLURAL</th></tr>
    </thead>
    <tbody>
      <tr><th class="case-name">Nominativ (wer?/was?)</th><td>die trau|rig</td><td>die trau|rig</td></tr>
      <tr><th class="case-name">Genitiv (wessen?)</th><td>der trau|rig</td><td>der trau|rig</td></tr>
      <tr><th class="case-name">Dativ (wem?)</th><td>der trau|rig</td><td>den trau|rig</td></tr>
      <tr><th class="case-name">Akkusativ (wen?/was?)</th><td>die trau|rig</td><td>die trau|rig</td></tr>
    </tbody>
  </table>
</section>

</body>
</html>
```